Skill Up Salary Up

Full Page
7.5 w x 10 h / 8 w x 10.75 h + .25" bleed
Full-Page Career Course Ad
Project Overview
• Goal: Create a visually attractive, modern, and uncluttered full-page magazine advertisement to list available career courses.
• Tone: Creative, professional, and attention-grabbing to prevent the reader from turning the page. The final design must prioritize readability.

Content Requirements
1. Header/Headline: Must be the primary focus. And grab peoples attention
2. Course Listing: A clear, well-organized list of the career courses.
________________________________________
Design & Aesthetic Directives
1. Layout & Readability (Crucial)
• The final ad must not look crowded or busy.
• Prioritize white space to make the text "breathe" and ensure the course list is easy to scan and read.
• Use a modern, clean, and professional typeface (font choice is critical for the aesthetic).
2. Visual Style
• Aim for a creative, modern, and fresh look. Avoid outdated or generic stock imagery/layouts.
3. Imagery/Graphic Element (Artist's Choice)
You have creative freedom regarding the main graphic element.
• Option A (Photography): Use a photo of a white male American with a collared shirt. The imagery should convey success, focus, or professional development.
• Option B (Vector/Illustration): Use a modern vector graphic, illustration, or abstract design. This could be used to symbolize growth, connection, or a career path.
The choice of graphic element is yours, but it must support the overall modern and uncrowded aesthetic.

Requirements
Must have
• Partial listing .. is part of the Vocational Horizon Course

```html
<!DOCTYPE html>
<html lang="en">
<head>
<meta charset="utf-8">
<title>Skill Up, Salary Up — Upcoming NVA Courses</title>
<link href="https://fonts.googleapis.com/css2?family=Lato:wght@700;900&family=Nunito+Sans:wght@600;700;800;900&display=swap" rel="stylesheet">
<style>
  :root{
    --purple:#5c1f87;
    --orange:#ec8a1c;
    --orange-soft:#f6c98f;
    --red:#d42a2f;
    --blue:#3a48a8;
    --green:#16875e;
    --ink:#14181f;
    --paper:#ffffff;
    --paper-shade:#e4e3e8;
    --bg:#d9d8d2;
  }
  *{box-sizing:border-box;margin:0;padding:0}
  html,body{width:1200px;height:1200px;overflow:hidden}
  body{background:var(--bg);font-family:"Nunito Sans",Arial,sans-serif;color:var(--ink);position:relative}
  .flyer{position:absolute;left:160px;top:15px;width:880px;height:1170px;background:linear-gradient(180deg,var(--paper) 0%,var(--paper) 45%,var(--paper-shade) 100%);overflow:hidden;box-shadow:0 6px 24px rgba(0,0,0,.18)}
  .growth-art{position:absolute;left:140px;top:420px;width:640px;height:640px;background:radial-gradient(circle at 50% 50%,rgba(200,200,210,.35),rgba(255,255,255,0) 70%)}
  .masthead{position:absolute;left:0;top:0;width:100%;height:170px;background:var(--purple);color:#fff;text-align:center;font-family:"Lato",Arial,sans-serif;padding-top:34px}
  .masthead .kicker{font-size:26px;font-weight:700;letter-spacing:.5px}
  .masthead h1{font-size:44px;font-weight:900;line-height:1.05;letter-spacing:.5px}
  .masthead .sub{font-size:21px;font-weight:700;margin-top:6px}
  .rule{position:absolute;left:0;top:178px;width:100%;height:3px;background:var(--purple)}
  .card{position:absolute}
  .card .frame{position:absolute;border-left:2px solid;border-bottom:2px solid}
  .tab{position:absolute;left:-2px;top:0;width:42px;height:34px}
  .tab i{position:absolute;left:22px;top:2px;width:30px;height:30px;border-radius:50%;background:#fff;border:2px solid;display:flex;align-items:center;justify-content:center}
  .tab svg{width:16px;height:16px}
  .title{font-weight:900;font-size:22px;text-transform:uppercase;line-height:1.25;letter-spacing:.2px}
  .lead{font-weight:800;font-size:20px;line-height:1.3}
  .pill{display:inline-block;color:#fff;font-weight:900;font-size:16px;padding:3px 12px;text-transform:uppercase}
  ul{list-style:none}
  li{font-weight:700;font-size:19px;line-height:1.55}
  li::before{content:"•";margin-right:8px}
  .inline li{display:inline-block;margin-right:26px;font-size:17px}
  .grid2{display:grid;grid-template-columns:1fr 1fr;column-gap:30px}

  .intro-card{position:absolute;left:30px;top:200px;width:820px;border-left:2px solid var(--orange);border-bottom:2px solid var(--orange);padding:4px 0 12px 62px}
  .intro-card .title{font-size:20px;letter-spacing:0}
  .intro-card .pill{margin:8px 0 14px}
  .intro-card .inline{margin-left:-40px}

  .c-orange .tab{background:var(--orange)} .c-orange .tab i{border-color:var(--orange);color:var(--orange)} .c-orange .title{color:var(--orange)} .c-orange li::before{color:var(--orange)} .c-orange .pill{background:var(--orange);box-shadow:0 6px 0 var(--orange-soft)}
  .c-red .frame{border-color:var(--red)} .c-red .tab{background:var(--red)} .c-red .tab i{border-color:var(--red);color:var(--red)} .c-red .title{color:var(--red)} .c-red li::before{color:var(--red)} .c-red .pill{background:var(--red)}
  .c-blue .frame{border-color:var(--blue)} .c-blue .tab{background:var(--blue)} .c-blue .tab i{border-color:var(--blue);color:var(--blue)} .c-blue .title{color:var(--blue)} .c-blue li::before{color:var(--blue)} .c-blue .pill{background:var(--blue)}
  .c-ink .frame{border-color:var(--ink)} .c-ink .tab{background:var(--ink)} .c-ink .tab i{border-color:var(--ink);color:var(--ink)} .c-ink .title{color:var(--ink)} .c-ink li::before{color:var(--ink)} .c-ink .pill{background:var(--ink)}
  .c-green .frame{border-color:var(--green)} .c-green .tab{background:var(--green)} .c-green .tab i{border-color:var(--green);color:var(--green)} .c-green .title{color:var(--green)} .c-green li::before{color:var(--green)} .c-green .pill{background:var(--green)}
  .body{position:absolute}
</style>
</head>
<body>
<main class="flyer">
  <div class="growth-art" role="img" aria-label="Faint illustration of a professional climbing toward a rising growth arrow"></div>

  <header class="masthead">
    <div class="kicker">SKILL UP, SALARY UP</div>
    <h1>UPCOMING NVA COURSES</h1>
    <div class="sub">MEN &amp; WOMEN | IN-PERSON &amp; REMOTE | PARTIAL SCHOLARSHIPS</div>
  </header>
  <div class="rule"></div>

  <section class="intro-card c-orange">
    <div class="tab"><i><svg viewBox="0 0 16 16" fill="none" stroke="currentColor" stroke-width="1.6"><rect x="2" y="5" width="12" height="8" rx="1"/><path d="M6 5V3h4v2"/></svg></i></div>
    <div class="title">Vocational Horizon Course Business Skills &amp; Knowledge to:</div>
    <div class="lead">Impress your interviewer Maximize Income<br>Start / Run Your Business</div>
    <span class="pill">4-5 Months Nov 2025</span>
    <ul class="inline">
      <li>Computers.</li><li>Marketing.</li><li>Finance.</li><li>Healthcare.</li><li>Sales.</li><li>Communication.</li>
      <li>Accounting.</li><li>Investments.</li><li>Real Estate.</li><li>Business Strategy.</li><li>LedgerBooks.</li>
    </ul>
  </section>

  <section class="card c-red" style="left:30px;top:440px;width:400px;height:300px">
    <div class="frame" style="left:0;top:0;width:400px;height:290px"></div>
    <div class="tab"><i><svg viewBox="0 0 16 16" fill="none" stroke="currentColor" stroke-width="1.6"><rect x="2" y="3" width="12" height="8" rx="1"/><path d="M6 14h4M8 11v3"/></svg></i></div>
    <div class="body" style="left:62px;top:4px;width:340px">
      <div class="title">Software, Web &amp; Apps:</div>
      <div class="lead" style="margin-top:6px">#2 Best Tech Job<br>National Careers Review 2025<br>Job Opportunities:</div>
      <ul style="margin-top:4px"><li>Computer Programmer.</li><li>Software Developer/Mobile.</li><li>Engineer / Developer (Apps).</li></ul>
      <div class="lead" style="margin-top:4px">Optional:</div>
      <ul><li>Bachelors in Prog.&amp; Tech.</li></ul>
    </div>
    <span class="pill" style="position:absolute;left:80px;top:276px">Nov 2025</span>
  </section>

  <section class="card c-blue" style="left:470px;top:470px;width:380px;height:270px">
    <div class="frame" style="left:0;top:0;width:380px;height:262px"></div>
    <div class="tab"><i><svg viewBox="0 0 16 16" fill="none" stroke="currentColor" stroke-width="1.6"><rect x="2" y="3" width="12" height="8" rx="1"/><path d="M4 14h8"/></svg></i></div>
    <div class="body" style="left:62px;top:4px;width:310px">
      <div class="title">IT Desktop &amp;<br>Networking Support:</div>
      <div class="lead" style="margin-top:6px">#2 Best Job<br>National Careers Review 2025<br>Masters IT:</div>
      <ul class="grid2" style="margin-top:4px"><li>Desktop OS.</li><li>Servers.</li><li>Networks.</li><li>Cloud.</li></ul>
    </div>
    <span class="pill" style="position:absolute;left:70px;top:248px">7 Months Dec 2025</span>
  </section>

  <section class="card c-ink" style="left:30px;top:795px;width:400px;height:300px">
    <div class="frame" style="left:0;top:0;width:400px;height:280px"></div>
    <div class="tab"><i><svg viewBox="0 0 16 16" fill="none" stroke="currentColor" stroke-width="1.6"><path d="M4 13V4h8v9z"/><path d="M6 7h4M6 10h4"/></svg></i></div>
    <div class="body" style="left:62px;top:4px;width:340px">
      <div class="title">Bookkeeping<br>LedgerBooks:</div>
      <div class="lead" style="margin-top:8px">Train for a quality job<br>Manage your own books</div>
      <ul style="margin-top:4px"><li>Finance Management.</li><li>Customer &amp; Vendor Mgmt.</li><li>Advanced Tools.</li></ul>
    </div>
    <span class="pill" style="position:absolute;left:80px;top:266px">5 Weeks Nov 2025</span>
  </section>

  <section class="card c-green" style="left:470px;top:795px;width:380px;height:300px">
    <div class="frame" style="left:0;top:0;width:380px;height:280px"></div>
    <div class="tab"><i><svg viewBox="0 0 16 16" fill="none" stroke="currentColor" stroke-width="1.6"><circle cx="8" cy="8" r="3"/><path d="M8 2v2M8 12v2M2 8h2M12 8h2"/></svg></i></div>
    <div class="body" style="left:62px;top:4px;width:310px">
      <div class="title">Office Suite-<br>Computers</div>
      <div class="lead" style="margin-top:8px">The New Job Prerequisite</div>
      <ul class="grid2" style="margin-top:4px"><li>Spreadsheets.</li><li>Email.</li><li>Documents.</li><li>Slides.</li></ul>
      <div class="lead" style="margin-top:6px">Computer lab<br>available to practice</div>
    </div>
    <span class="pill" style="position:absolute;left:70px;top:266px">5 Weeks Dec 2025</span>
  </section>
</main>
</body>
</html>
```